Cell phone repair

you can please design me business card

size 3.5" x 2"

colors blue and red

fixit rapid logo (you get from my website fixitrapidco.example )

"We Come To You!

It is very simple! You tell us what phone you have, And we come to fix it."

phone number: 555.248.3906

website: www.fixitrapidco.example

email: info@fixitrapidco.example

```html
<!DOCTYPE html>
<html lang="en">
<head>
<meta charset="utf-8">
<title>Fixit Rapid – Business Card</title>
<link href="https://fonts.googleapis.com/css2?family=Exo+2:ital,wght@0,600;0,700;1,700&family=Open+Sans:wght@400;600&display=swap" rel="stylesheet">
<style>
  :root {
    --bg: #1b1b1b;
    --blue: #2aa6dc;
    --red: #e8262c;
    --ink: #131313;
    --white: #ffffff;
  }
  * { box-sizing: border-box; margin: 0; padding: 0; }
  html, body { width: 1200px; height: 1200px; overflow: hidden; background: var(--bg); }
  .stage { position: relative; width: 1200px; height: 1200px; }

  .card {
    position: absolute; left: 150px; width: 900px; height: 514px;
    border-radius: 22px; overflow: hidden;
    box-shadow: 0 10px 30px rgba(0,0,0,.5);
  }

  /* Front */
  .card--front {
    top: 50px;
    background: linear-gradient(100deg, var(--blue) 0%, #5aa0c4 18%, #a0807e 40%, #e0473f 62%, var(--red) 100%);
  }
  .circuit-field {
    position: absolute; left: 0; top: 0; width: 300px; height: 100%;
    background: linear-gradient(90deg, rgba(255,255,255,.18), rgba(255,255,255,0));
  }
  .front-brand {
    position: absolute; left: 260px; top: 200px;
    display: flex; align-items: center; gap: 26px;
  }
  .front-brand__name {
    font-family: "Exo 2", sans-serif; font-weight: 700; font-size: 56px;
    color: var(--white); letter-spacing: .5px;
  }
  .front-brand__mark { width: 60px; height: 60px; border: 5px solid var(--white); border-radius: 8px; }
  .front-url {
    position: absolute; left: 0; right: 0; top: 370px; text-align: center;
    font-family: "Exo 2", sans-serif; font-weight: 600; font-size: 19px;
    letter-spacing: 2px; color: var(--white);
  }

  /* Back */
  .card--back { top: 624px; background: var(--ink); }
  .back-tagline {
    position: absolute; left: 80px; top: 60px;
    font-family: "Exo 2", sans-serif; font-weight: 700; font-size: 36px; color: var(--white);
  }
  .back-brand {
    position: absolute; left: 470px; top: 140px;
    display: flex; align-items: center; gap: 22px;
  }
  .back-brand__name {
    font-family: "Exo 2", sans-serif; font-weight: 700; font-size: 46px; color: var(--blue);
  }
  .back-brand__mark { width: 56px; height: 56px; border: 5px solid var(--red); border-radius: 8px; }
  .pitch { position: absolute; left: 66px; top: 248px; }
  .pitch__head {
    font-family: "Open Sans", sans-serif; font-weight: 600; font-size: 38px;
    color: var(--red); line-height: 1.1;
  }
  .pitch__body {
    font-family: "Open Sans", sans-serif; font-weight: 400; font-size: 21px;
    color: var(--blue); margin-top: 2px;
  }
  .rule { position: absolute; left: 56px; right: 56px; top: 342px; height: 3px; background: var(--blue); }
  .call { position: absolute; left: 60px; top: 358px; }
  .call__label { font-family: "Exo 2", sans-serif; font-weight: 700; font-size: 26px; }
  .call__label .call-blue { color: var(--blue); }
  .call__label .call-red { color: var(--red); }
  .call__number {
    font-family: "Exo 2", sans-serif; font-weight: 700; font-style: italic;
    font-size: 46px; color: var(--white); letter-spacing: 1px; line-height: 1.1;
  }
  .contacts { position: absolute; left: 540px; top: 392px; list-style: none; }
  .contacts li {
    display: flex; align-items: center; gap: 14px; margin-bottom: 8px;
    font-family: "Open Sans", sans-serif; font-size: 22px; color: var(--white);
  }
  .contacts svg { width: 26px; height: 26px; flex: none; }
</style>
</head>
<body>
<main class="stage">

  <section class="card card--front" aria-label="Business card front">
    <div class="circuit-field" role="img" aria-label="Faint circuit board line pattern"></div>
    <div class="front-brand">
      <span class="front-brand__name">Fixit Rapid</span>
      <span class="front-brand__mark" aria-hidden="true"></span>
    </div>
    <p class="front-url">WWW.FIXITRAPIDCO.EXAMPLE</p>
  </section>

  <section class="card card--back" aria-label="Business card back">
    <h2 class="back-tagline">We Come To You!</h2>
    <div class="back-brand">
      <span class="back-brand__name">Fixit Rapid</span>
      <span class="back-brand__mark" aria-hidden="true"></span>
    </div>
    <div class="pitch">
      <p class="pitch__head">It is very simple!</p>
      <p class="pitch__body">You tell us what phone you have, And we come to fix it.</p>
    </div>
    <div class="rule"></div>
    <div class="call">
      <p class="call__label"><span class="call-blue">CALL</span> <span class="call-red">US</span></p>
      <p class="call__number">555.248.3906</p>
    </div>
    <ul class="contacts">
      <li>
        <svg viewBox="0 0 24 24" fill="none" stroke="#e8262c" stroke-width="1.8" aria-hidden="true">
          <circle cx="12" cy="12" r="10"/><ellipse cx="12" cy="12" rx="4.5" ry="10"/>
          <line x1="2" y1="12" x2="22" y2="12"/><line x1="4" y1="7" x2="20" y2="7"/><line x1="4" y1="17" x2="20" y2="17"/>
        </svg>
        www.fixitrapidco.example
      </li>
      <li>
        <svg viewBox="0 0 24 24" fill="#e8262c" aria-hidden="true">
          <path d="M2 5h20v14H2z"/><path d="M2 5l10 8 10-8" fill="none" stroke="#131313" stroke-width="1.6"/>
        </svg>
        info@fixitrapidco.example
      </li>
    </ul>
  </section>

</main>
</body>
</html>
```